Remodeling brochure

We need an informative homeowner friendly brochure detailing our company and things we do. We are looking for an initial setup and ideas (# of pages, etc) and then we will send more content. We are uploading our logo design. We are a high end remodeling company specializing in kitchen & bath remodels. We sell ourselves on customer communication and attention to detail in our designs and remodels.

Target Market(s)

Residential homeowners

Contact Information for Business Card

Modern and attention grabbing

Requirements
Must have
• Name- Hearth & Tile Crafters<br/>Address- 782 NW Larkspur Lane Suite #217<br/> Ankeny, Iowa 50894<br/>Phone- 515-482-7395<br/>email-htcraftersmidwest@pinemail.net

```html
<!DOCTYPE html>
<html lang="en">
<head>
<meta charset="utf-8">
<title>Hearth &amp; Tile Crafters – Brochure Spread</title>
<link href="https://fonts.googleapis.com/css2?family=Montserrat:wght@300;400;500;600;700&display=swap" rel="stylesheet">
<style>
  :root{
    --backdrop:#5b5b5b;
    --paper:#ffffff;
    --brand-blue:#1565d8;
    --brand-blue-deep:#0a3fb8;
    --brand-sky:#1e90e0;
    --ink:#1b1e24;
    --ink-soft:#4a4f57;
    --teal:#0f5e63;
  }
  *{box-sizing:border-box;margin:0;padding:0}
  html,body{width:1200px;height:2656px;overflow:hidden}
  body{background:var(--backdrop);font-family:"Montserrat",sans-serif;position:relative}
  .spread{position:absolute;left:50px;top:940px;width:1100px;height:776px;background:var(--paper);box-shadow:0 20px 50px rgba(0,0,0,.35);overflow:hidden}
  .spread::after{content:"";position:absolute;left:550px;top:0;width:1px;height:100%;background:rgba(0,0,0,.06)}
  .brand{position:absolute;display:flex;align-items:center;color:var(--brand-blue);font-weight:600;letter-spacing:.3px;white-space:nowrap}
  .brand__mark{background:var(--brand-blue);flex:none}
  .brand--cover{right:62px;top:48px;height:60px;font-size:23px;gap:12px}
  .brand--cover .brand__mark{width:46px;height:46px}
  .brand--back{left:208px;top:686px;font-size:8.5px;gap:5px}
  .brand--back .brand__mark{width:16px;height:16px}
  .cover-photo{position:absolute;left:380px;top:150px;width:720px;height:438px;
    background:linear-gradient(100deg,#6b4b3a 0%,#b9a89a 14%,#e9ecef 32%,#f6f7f8 55%,#d9dcdf 78%,#bfc4c8 100%)}
  .cover-band{position:absolute;left:380px;top:588px;width:720px;height:118px;
    background:linear-gradient(90deg,var(--brand-sky),var(--brand-blue) 45%,var(--brand-blue-deep));color:#fff;text-align:center}
  .cover-band__title{margin-top:28px;font-size:29px;font-weight:700;letter-spacing:4px}
  .cover-band__sub{margin-top:6px;font-size:22px;font-weight:300;letter-spacing:1px}
  .cover-web{position:absolute;left:380px;width:720px;top:734px;text-align:center;font-size:11px;letter-spacing:4px;color:var(--ink)}
  .back-photo{position:absolute;left:66px;top:67px;width:366px;height:225px;
    background:linear-gradient(90deg,#8a5a3b 0%,#a97752 25%,#e9e6e1 45%,#f3f2ef 70%,#d8d2c9 100%)}
  .accent-tile{position:absolute;left:380px;top:145px;width:52px;height:178px;background:var(--teal);opacity:.8;z-index:2}
  .accent-frame{position:absolute;left:340px;top:98px;width:153px;height:226px;border:1px solid var(--brand-blue-deep);z-index:2}
  .section-title{position:absolute;left:66px;font-size:16px;font-weight:600;color:var(--ink);letter-spacing:.3px}
  .section-title span{color:var(--brand-sky)}
  .why{top:352px}
  .contact{top:548px}
  .intro{position:absolute;left:66px;top:380px;width:268px;font-size:8.2px;line-height:1.45;color:var(--ink-soft);text-align:justify}
  .checklist{position:absolute;left:66px;top:448px;list-style:none;font-size:9px;font-weight:500;color:var(--ink)}
  .checklist li{display:flex;align-items:center;gap:6px;height:16px}
  .checklist svg{width:8px;height:8px}
  .contact-list{position:absolute;left:66px;top:576px;list-style:none;font-size:11px;color:var(--ink-soft)}
  .contact-list li{display:flex;gap:8px;margin-bottom:9px;line-height:1.4}
  .contact-list svg{width:9px;height:9px;margin-top:3px;flex:none}
</style>
</head>
<body>
<main class="spread">
  <section class="back-panel">
    <div class="back-photo" role="img" aria-label="Photo of a bright dining area with white chairs and a wood-panelled wall"></div>
    <div class="accent-frame"></div>
    <div class="accent-tile"></div>

    <h2 class="section-title why">WHY <span>CHOOSE US</span></h2>
    <p class="intro">The number one reason why you should partner with us is that we are the only company in the state licensed to do warranty work. With us, you can be confident that your projects are in safe, dependable hands. Here are more reasons to choose us:</p>
    <ul class="checklist">
      <li><svg viewBox="0 0 10 10"><path d="M1 5l3 3 5-7" fill="none" stroke="#1e90e0" stroke-width="1.6"/></svg>Fully Insured and Licensed Business</li>
      <li><svg viewBox="0 0 10 10"><path d="M1 5l3 3 5-7" fill="none" stroke="#1e90e0" stroke-width="1.6"/></svg>Listed on Home Pro Directory</li>
      <li><svg viewBox="0 0 10 10"><path d="M1 5l3 3 5-7" fill="none" stroke="#1e90e0" stroke-width="1.6"/></svg>Serves Residential and Commercial Clients</li>
      <li><svg viewBox="0 0 10 10"><path d="M1 5l3 3 5-7" fill="none" stroke="#1e90e0" stroke-width="1.6"/></svg>Various Payment Options Accepted</li>
    </ul>

    <h2 class="section-title contact">CONTACT <span>INFO</span></h2>
    <ul class="contact-list">
      <li><svg viewBox="0 0 10 10"><path d="M5 10C2 6 1.5 4.8 1.5 3.5a3.5 3.5 0 017 0C8.5 4.8 8 6 5 10z" fill="#1e90e0"/></svg><span>782 NW Larkspur Lane Suite #217<br>Ankeny, Iowa 50894</span></li>
      <li><svg viewBox="0 0 10 10"><circle cx="5" cy="5" r="4.5" fill="#1e90e0"/></svg><span>515-482-7395</span></li>
      <li><svg viewBox="0 0 10 10"><rect x=".5" y="2" width="9" height="6" fill="none" stroke="#1e90e0"/><path d="M.5 2l4.5 3.5L9.5 2" fill="none" stroke="#1e90e0"/></svg><span>CustomerSupport@htcraftersia.com</span></li>
      <li><svg viewBox="0 0 10 10"><circle cx="5" cy="5" r="4" fill="none" stroke="#1e90e0"/><path d="M1 5h8M5 1v8" stroke="#1e90e0"/></svg><span>www.htcraftersia.com</span></li>
    </ul>
    <div class="brand brand--back"><span class="brand__mark"></span>HEARTH &amp; TILE CRAFTERS</div>
  </section>

  <section class="cover-panel">
    <div class="brand brand--cover"><span class="brand__mark"></span>HEARTH &amp; TILE CRAFTERS</div>
    <div class="cover-photo" role="img" aria-label="Photo of a bright modern kitchen with marble island, brass faucet, pendant bulbs and large windows"></div>
    <div class="cover-band">
      <h1 class="cover-band__title">WE SPECIALIZE IN</h1>
      <p class="cover-band__sub">KITCHEN AND BATHROOM RENOVATIONS</p>
    </div>
    <p class="cover-web">www.htcraftersia.com</p>
  </section>
</main>
</body>
</html>
```